Do i have coronavirus, flue or cold?

Using information from QRV and government agencies we want to make a easy to read infographic helping patients see if they have coronavirus, the flu or a cold. Using a flow diagram or whatever you think will make it easy to read and digest for the average lamen.

Information is in the word document and in the chart.

We are www.tovipharm.co.uk attached is our brand guidelines, we will be putting this infographic on our website and email/sms it to all of our 300,000 patients.

```html
<!DOCTYPE html>
<html lang="en">
<head>
<meta charset="utf-8">
<title>Do I have coronavirus, flu or cold?</title>
<link rel="stylesheet" href="https://fonts.googleapis.com/css2?family=Poppins:wght@400;500;700&display=swap">
<style>
  :root {
    --page: #4f5bc2;
    --navy: #3f479e;
    --header: #3f469d;
    --ice: #ecf4f6;
    --periwinkle: #7582c6;
    --flu-band: #7788c4;
    --salmon: #f5a07d;
    --cold-band: #f5a482;
    --red: #e3262b;
    --white: #ffffff;
    --line: #1f2150;
  }
  * { box-sizing: border-box; margin: 0; padding: 0; }
  html, body {
    width: 1200px; height: 1200px; overflow: hidden;
    background: var(--page);
    font-family: "Poppins", sans-serif;
  }
  .infographic {
    position: absolute;
    left: 278px; top: 20px;
    width: 894px; height: 1609px;
    transform: scale(0.7209);
    transform-origin: 0 0;
    box-shadow: 0 10px 30px rgba(20, 24, 80, 0.25);
    overflow: hidden;
  }
  .band { position: absolute; left: 0; width: 894px; }
  .band--header { top: 0; height: 155px; background: var(--header); }
  .band--corona { top: 155px; height: 486px; background: var(--ice); }
  .band--flu { top: 641px; height: 484px; background: var(--flu-band); }
  .band--cold { top: 1125px; height: 484px; background: var(--cold-band); }

  .main-title {
    position: absolute; left: 0; top: 20px; width: 894px;
    text-align: center; color: var(--white);
    font-weight: 700; font-size: 50px; line-height: 55px; letter-spacing: 3px;
  }
  .section-title {
    position: absolute; font-weight: 700; font-size: 58px; line-height: 1;
    color: var(--navy); letter-spacing: 0.5px; white-space: nowrap;
  }
  .section-title--flu { color: var(--white); }
  .symptoms-heading {
    position: absolute; width: 200px; text-align: center;
    font-weight: 700; font-size: 34px; line-height: 1; color: var(--red);
    letter-spacing: 0.5px;
  }
  .symptom {
    position: absolute; width: 182px;
    display: flex; align-items: center; justify-content: center; text-align: center;
    border-radius: 3px; white-space: nowrap;
    font-size: 16.5px; line-height: 17px; letter-spacing: 0.6px; color: var(--white);
  }
  .symptom--periwinkle { background: var(--periwinkle); }
  .symptom--salmon { background: var(--salmon); }
  .symptom--navy { background: var(--navy); }
  .symptom--ice { background: var(--ice); color: var(--periwinkle); }

  .illustration { position: absolute; border-radius: 50%; }
  .illustration--corona {
    left: 115px; top: 302px; width: 280px; height: 290px;
    background: radial-gradient(circle at 55% 45%, #ffffff 0%, #dfe8f3 55%, #4a4fa8 100%);
  }
  .illustration--flu {
    left: 485px; top: 747px; width: 290px; height: 340px;
    background: radial-gradient(circle at 50% 55%, #ffffff 0%, #e6ecf6 50%, #4147a0 100%);
  }
  .illustration--cold {
    left: 113px; top: 1250px; width: 270px; height: 355px;
    background: radial-gradient(circle at 50% 50%, #ffffff 0%, #edf3f6 55%, #3f479e 100%);
  }
  .connectors { position: absolute; left: 0; top: 0; }
</style>
</head>
<body>
<main class="infographic">
  <div class="band band--header"></div>
  <div class="band band--corona"></div>
  <div class="band band--flu"></div>
  <div class="band band--cold"></div>

  <h1 class="main-title">DO I HAVE CORONAVIRUS,<br>FLU OR COLD?</h1>

  <h2 class="section-title" style="left:55px; top:190px;">CORONAVIRUS</h2>
  <div class="illustration illustration--corona" role="img" aria-label="Illustration of a woman in a scarf and face mask coughing into her hand"></div>
  <h3 class="symptoms-heading" style="left:571px; top:235px;">SYMTOMS</h3>
  <div class="symptom symptom--periwinkle" style="left:579px; top:275px; height:47px;">FEVER</div>
  <div class="symptom symptom--salmon" style="left:579px; top:338px; height:38px;">DRY COUGH</div>
  <div class="symptom symptom--periwinkle" style="left:579px; top:392px; height:38px;">SHORTNESS<br>OF BREATH</div>
  <div class="symptom symptom--salmon" style="left:579px; top:446px; height:40px;">TIREDNESS</div>
  <div class="symptom symptom--periwinkle" style="left:579px; top:504px; height:39px;">MUSCLE ACHES</div>
  <div class="symptom symptom--salmon" style="left:579px; top:564px; height:39px;">SORE THROAT</div>

  <h2 class="section-title section-title--flu" style="left:745px; top:686px;">FLU</h2>
  <h3 class="symptoms-heading" style="left:115px; top:695px;">SYMTOMS</h3>
  <div class="symptom symptom--navy" style="left:129px; top:744px; height:46px;">HIGH FEVER</div>
  <div class="symptom symptom--salmon" style="left:129px; top:806px; height:38px;">COUGH</div>
  <div class="symptom symptom--navy" style="left:129px; top:860px; height:38px;">HEADACHES</div>
  <div class="symptom symptom--salmon" style="left:129px; top:914px; height:40px;">SHORTNESS<br>OF BREATH</div>
  <div class="symptom symptom--navy" style="left:129px; top:973px; height:38px;">MUSCLE ACHES</div>
  <div class="symptom symptom--salmon" style="left:129px; top:1032px; height:38px;">SORE THROAT</div>
  <div class="illustration illustration--flu" role="img" aria-label="Illustration of a man with a headache and a thermometer in his mouth, wrapped in a jacket"></div>

  <h2 class="section-title" style="left:55px; top:1186px;">COLD</h2>
  <div class="illustration illustration--cold" role="img" aria-label="Illustration of a woman in a striped scarf sneezing while holding a hot drink"></div>
  <h3 class="symptoms-heading" style="left:562px; top:1195px;">SYMTOMS</h3>
  <div class="symptom symptom--periwinkle" style="left:570px; top:1245px; height:47px;">SNEEZING</div>
  <div class="symptom symptom--ice" style="left:570px; top:1308px; height:38px;">RUNY NOSE</div>
  <div class="symptom symptom--periwinkle" style="left:570px; top:1362px; height:38px;">MODERATE COUGHS</div>
  <div class="symptom symptom--ice" style="left:570px; top:1416px; height:39px;">MILD MUSCLE ACES</div>
  <div class="symptom symptom--periwinkle" style="left:570px; top:1474px; height:39px;">LOSE OF TASTE</div>
  <div class="symptom symptom--ice" style="left:570px; top:1534px; height:38px;">SORE THROAT</div>

  <svg class="connectors" width="894" height="1609" viewBox="0 0 894 1609" aria-hidden="true">
    <g fill="none" stroke="var(--line)" stroke-width="2">
      <path d="M570 299 H542 Q530 299 530 311 V572 Q530 584 542 584 H570"/>
      <path d="M530 357 H570 M530 411 H570 M530 466 H570 M530 523 H570"/>
      <path d="M435 441 H530"/>
      <path d="M320 767 H348 Q360 767 360 779 V1039 Q360 1051 348 1051 H320"/>
      <path d="M320 825 H360 M320 879 H360 M320 934 H360 M320 992 H360"/>
      <path d="M360 909 H455"/>
      <path d="M562 1269 H534 Q522 1269 522 1281 V1541 Q522 1553 534 1553 H562"/>
      <path d="M522 1327 H562 M522 1381 H562 M522 1435 H562 M522 1494 H562"/>
      <path d="M426 1411 H522"/>
    </g>
  </svg>
</main>
</body>
</html>
```